verdant terraces simple classy business card design

my name is owen harlow and I run a gardening business aimed at high class verdant terraces. the business name is verdant terraces and our logo was designed on pixel forum .My clientel are anything from residential homes to businesses. I take pride in my work and know that I offer a service like no other in my area.
The business card will be used to represent my business and I want it to be not only rememberable, but simplistic and modern. Eye catching too. Of course I would like it relatable to gardening and appealing to the correct clientel - those being garden enthusiasts, prestigious homes and businesses that are after top of the line gardening services like no other on the market.
I am not a typical lawn mowing business so I don't want a typical card design that represents that. The gardens I work with are generally million dollar properties with owners who are very garden proud looking for upkeep and guidance from me along with sometimes whole new garden designs. I want the business cards to show to my clients that I take pride, as they do, in their garden. And I want them to know from my card that I am a professional, qualified horticulturist offering them a top of the line service for life. I want them to refer my business on. I want them to look at my business card and see class and professionalism in a modern unique bold way.
The card should be simple with the possibility of the logo on the front being embossed/debossed and my details on the back the card should have a organic garden feel it's very important to me that it is absolutely perfect
I am also very open to ideas and suggestions so look forward to seeing the designs. the business logo has been supplied with this project and I want the card to be double sided

Contact info is
Owen Harlow - Managing Director / Horticulturist
Phone : 0481 526 704
Email: owenharlow@verdantterraces.com.au

Target Market(s)

high class gardens residential and commercial

Industry/Entity Type

Gardener

Contact Information for Business Card

Contact info is
Phone : 0481 526 704

PLEASE MAKE CARD DOUBLE SIDED

Requirements
Must have
• organic simple classy modern feel
• must flow with the current logo that has been supplied with this project
• Double sided
• Must explain in a simple way that I deal with high end gardens and I'm a qualified horticulturist
Nice to have
• embossed debossed logo
Should not have
• shouldn't be to busy or cheap looking

```html
<!DOCTYPE html>
<html lang="en">
<head>
<meta charset="utf-8">
<title>Verdant Terraces – Business Card Set</title>
<link href="https://fonts.googleapis.com/css2?family=Exo+2:wght@700&family=PT+Sans:wght@400&display=swap" rel="stylesheet">
<style>
  :root {
    --leaf: #4cc63a;
    --leaf-soft: #8fdc83;
    --leaf-pale: #d9f3d4;
    --paper: #fafbfa;
    --page: #ffffff;
    --shadow: rgba(0, 0, 0, 0.55);
  }
  * { box-sizing: border-box; margin: 0; padding: 0; }
  html, body {
    width: 1200px;
    height: 926px;
    overflow: hidden;
    background: var(--page);
  }
  .canvas {
    position: relative;
    width: 1200px;
    height: 926px;
  }
  .card {
    position: absolute;
    background: var(--paper);
    box-shadow: 8px 8px 8px var(--shadow);
    overflow: hidden;
  }
  .card__frame {
    position: absolute;
    border: 7px solid var(--leaf);
    pointer-events: none;
    z-index: 3;
  }
  .wordmark {
    position: absolute;
    z-index: 2;
    text-align: center;
    font-family: "PT Sans", sans-serif;
    font-weight: 400;
    color: var(--leaf);
    line-height: 1;
  }
  .wordmark__mark {
    display: block;
    margin: 0 auto;
    border-radius: 50%;
    background: var(--leaf);
  }
  .wordmark__name {
    display: block;
    letter-spacing: 0.06em;
  }
  .wordmark__sub {
    display: block;
    letter-spacing: 0.62em;
    padding-left: 0.62em;
  }
  .tree-art {
    position: absolute;
    z-index: 1;
    background: radial-gradient(ellipse at 55% 45%, var(--leaf-soft) 0%, var(--leaf-pale) 60%, rgba(217, 243, 212, 0) 78%);
  }

  /* Portrait card */
  .card--portrait { left: 12px; top: 12px; width: 437px; height: 892px; }
  .card--portrait .card__frame { left: 23px; top: 23px; right: 23px; bottom: 23px; }
  .card--portrait .wordmark { left: 0; right: 0; top: 42px; }
  .card--portrait .wordmark__mark { width: 62px; height: 62px; margin-bottom: 8px; }
  .card--portrait .wordmark__name { font-size: 32px; }
  .card--portrait .wordmark__sub { font-size: 18px; margin-top: 5px; }
  .card--portrait .tree-art { left: 23px; top: 186px; width: 360px; height: 683px; }

  /* Landscape front */
  .card--front { left: 544px; top: 37px; width: 625px; height: 358px; }
  .card--front .card__frame { left: 14px; top: 14px; right: 14px; bottom: 14px; }
  .card--front .wordmark { left: 0; right: 0; top: 100px; }
  .card--front .wordmark__mark { width: 74px; height: 74px; margin-bottom: 14px; }
  .card--front .wordmark__name { font-size: 36px; }
  .card--front .wordmark__sub { font-size: 20px; margin-top: 8px; }

  /* Landscape back */
  .card--back { left: 551px; top: 484px; width: 626px; height: 355px; }
  .card--back .card__frame { left: 14px; top: 14px; right: 14px; bottom: 14px; }
  .card--back .tree-art { left: 345px; top: 21px; width: 260px; height: 313px; }
  .contact__name {
    position: absolute;
    z-index: 2;
    left: 40px;
    top: 92px;
    font-family: "Exo 2", sans-serif;
    font-weight: 700;
    font-size: 36px;
    letter-spacing: 0.02em;
    color: var(--leaf);
  }
  .contact__role {
    position: absolute;
    z-index: 2;
    left: 44px;
    top: 136px;
    font-family: "PT Sans", sans-serif;
    font-size: 15.5px;
    color: var(--leaf);
  }
  .contact__line {
    position: absolute;
    z-index: 2;
    left: 36px;
    display: flex;
    align-items: center;
    gap: 9px;
    font-family: "PT Sans", sans-serif;
    font-size: 15.5px;
    color: var(--leaf);
  }
  .contact__line--phone { top: 205px; }
  .contact__line--email { top: 257px; }
  .contact__icon { width: 35px; height: 35px; flex: none; }
</style>
</head>
<body>
<main class="canvas">

  <section class="card card--portrait" aria-label="Tall card">
    <div class="wordmark">
      <span class="wordmark__mark"></span>
      <span class="wordmark__name">VERDANT</span>
      <span class="wordmark__sub">TERRACES</span>
    </div>
    <div class="tree-art" role="img" aria-label="Large leafy green tree illustration"></div>
    <div class="card__frame"></div>
  </section>

  <section class="card card--front" aria-label="Card front">
    <div class="wordmark">
      <span class="wordmark__mark"></span>
      <span class="wordmark__name">VERDANT</span>
      <span class="wordmark__sub">TERRACES</span>
    </div>
    <div class="card__frame"></div>
  </section>

  <section class="card card--back" aria-label="Card back">
    <div class="tree-art" role="img" aria-label="Leafy green tree branch illustration"></div>
    <h1 class="contact__name">OWEN HARLOW</h1>
    <p class="contact__role">Managing Director / Horticulturist</p>
    <p class="contact__line contact__line--phone">
      <svg class="contact__icon" viewBox="0 0 36 36" aria-hidden="true">
        <circle cx="18" cy="18" r="18" fill="var(--leaf)"/>
        <path d="M12.5 9.5c1-.6 2-.4 2.6.6l1.6 2.8c.5.9.3 1.9-.5 2.5l-1.1.8c.8 2 2.5 3.9 4.5 4.8l.9-1.1c.6-.8 1.6-1 2.5-.5l2.8 1.6c1 .6 1.2 1.7.6 2.6l-.8 1.2c-.8 1.2-2.3 1.7-3.7 1.3-5.2-1.6-9.4-5.8-11-11-.4-1.4.1-2.9 1.3-3.7z" fill="var(--paper)"/>
      </svg>
      <span>0481 526 704</span>
    </p>
    <p class="contact__line contact__line--email">
      <svg class="contact__icon" viewBox="0 0 36 36" aria-hidden="true">
        <circle cx="18" cy="18" r="18" fill="var(--leaf)"/>
        <rect x="9" y="11.5" width="18" height="13" rx="1.2" fill="var(--paper)"/>
        <path d="M9.5 12.5 18 19l8.5-6.5" fill="none" stroke="var(--leaf)" stroke-width="1.6"/>
      </svg>
      <span>owenharlow@verdantterraces.com.au</span>
    </p>
    <div class="card__frame"></div>
  </section>

</main>
</body>
</html>
```